Vehicles Brochure Diagram

Task Outline
Create diagrams for our new vehicles brochures

Task Description

Who are we:
TLR is New Zealand's largest Business Group Buying organisation, helping organisations nationwide reduce their running costs. We offer members the best deals from over 100 Contracted Suppliers, anything from vehicles, stationery to electronics and coffee.

The project:
We need 2 diagrams to illustrate the benefits of our vehicle services. The diagram will be used in our brochures (example attached)

1. A Diagram illustrating/explaining the elements that are involved in purchasing a new car & how our service ties it all together to provide the best solution.
- Please see the Diagram 1 PDF for a rough wireframe of the elements involved

2. Another small diagram inserted on an separate page to demonstrate how our services can increase safety & profit and reduce costs & risks (PDF: Diagram 2 Details)

The design needs to be clean, clear and simple that it’s easy to understand within a few seconds of looking at it. Feel free to explore with different elements in the realm of infographics, flowcharts & diagrams to best communicate the idea visually.
Updates

Just thought I’ll share some of the feedback we’re giving tosubmissions that have been coming through to help with new submissions

-Challenge & be creative about the ways you demonstratethe elements

-We don’t want to see your design replicating the ones that isdrawn. The purpose of it is only to provide you with the content in context

-We can’t emphasis enough that the style pdf is only areference and not the look you should imitate. 

If you have any question please feel free to contact me.Looking forward to see your designs!

Reason: We're keen to see more approaches & creative ways of interpreting the content rather than a standard cycle diagram. Entries so far have been good but quite literal, we will provide feedback to help steer it in the right direction.

Target Market(s)

Business professionals, Decision makers on a corporate level & prospects.

Industry/Entity Type

Electronics

Requirements
Must have

• Likes – simple, clean & clear, uncluttered

Dislikes – Overcrowded images, text, & colours. Overly expressive typeface. Please no literal illustration of our sketches or colored version of our sketch.

Font: -Myriad Pro

Colour: Please refer to the color palette in the ‘Diagram Color & Style’ PDF

The brochures are attached with content to provide context that might inform the design better,

Dimensions & the amount of space you have to work with will also be highlighted

```html
<!DOCTYPE html>
<html lang="en">
<head>
<meta charset="utf-8">
<title>Vehicle Services Benefits Diagram</title>
<link href="https://fonts.googleapis.com/css2?family=Arvo:wght@700&family=Montserrat:wght@600&display=swap" rel="stylesheet">
<style>
  :root {
    --orange-light: #f7dca8;
    --orange-mid: #f2aa44;
    --orange-deep: #f2991c;
    --green-deep: #4a9a3c;
    --green-mid: #62b04e;
    --green-light: #92cd7f;
    --heading-brown: #8a3a10;
    --heading-green: #2f4a2c;
    --ring-green: #58a845;
    --ring-orange: #f29a2a;
    --icon-grey: #4a4a4a;
    --label-white: #ffffff;
    --page-bg: #ffffff;
  }
  html, body {
    margin: 0;
    padding: 0;
    width: 1200px;
    height: 1050px;
    overflow: hidden;
    background: var(--page-bg);
  }
  .diagram {
    position: relative;
    width: 1200px;
    height: 1050px;
  }
  .diagram__shape {
    position: absolute;
    left: 0;
    top: 0;
  }
  .heading {
    position: absolute;
    margin: 0;
    font-family: "Arvo", "Rockwell", serif;
    font-weight: 700;
    font-size: 58px;
    line-height: 62px;
  }
  .heading--increase { left: 252px; top: 152px; color: var(--heading-brown); }
  .heading--decrease { left: 630px; top: 797px; color: var(--heading-green); }
  .benefit {
    position: absolute;
    display: flex;
    align-items: center;
    gap: 18px;
    transform: translateY(-50%);
  }
  .benefit__icon {
    box-sizing: border-box;
    width: 92px;
    height: 92px;
    border-radius: 50%;
    background: #fff;
    border: 6px solid var(--ring-green);
    display: flex;
    align-items: center;
    justify-content: center;
    flex: none;
  }
  .benefit--reduce .benefit__icon { border-color: var(--ring-orange); }
  .benefit__icon svg { width: 48px; height: 48px; fill: var(--icon-grey); }
  .benefit__label {
    font-family: "Montserrat", "Helvetica Neue", Arial, sans-serif;
    font-weight: 600;
    font-size: 24px;
    line-height: 34px;
    color: var(--label-white);
    text-transform: uppercase;
    letter-spacing: 0.2px;
  }
  .col-left { left: 246px; }
  .col-right { left: 614px; }
</style>
</head>
<body>
<main class="diagram">
  <svg class="diagram__shape" width="1200" height="1050" viewBox="0 0 1200 1050" aria-hidden="true">
    <defs>
      <linearGradient id="increaseFill" x1="0.2" y1="0" x2="0.6" y2="1">
        <stop offset="0" stop-color="var(--orange-light)"/>
        <stop offset="0.45" stop-color="var(--orange-mid)"/>
        <stop offset="1" stop-color="var(--orange-deep)"/>
      </linearGradient>
      <linearGradient id="decreaseFill" x1="0" y1="0" x2="0" y2="1">
        <stop offset="0" stop-color="var(--green-deep)"/>
        <stop offset="0.4" stop-color="var(--green-mid)"/>
        <stop offset="1" stop-color="var(--green-light)"/>
      </linearGradient>
    </defs>
    <path class="arrow-up" d="M175 151 L600 45 L1025 151 L995 151 L995 528 L205 528 L205 151 Z" fill="url(#increaseFill)"/>
    <path class="arrow-down" d="M205 535 L995 535 L995 915 L1025 915 L600 1020 L175 915 L205 915 Z" fill="url(#decreaseFill)"/>
  </svg>

  <h2 class="heading heading--increase">Increase<br>Your</h2>

  <div class="benefit col-right" style="top:242px">
    <span class="benefit__icon"><svg viewBox="0 0 48 48"><path d="M18 6h12l-4 7h-4z"/><path d="M24 14c-10 0-16 12-16 20 0 6 4 9 16 9s16-3 16-9c0-8-6-20-16-20z"/><text x="24" y="37" font-size="14" font-family="Arial" font-weight="700" text-anchor="middle" fill="#fff">$</text></svg></span>
    <span class="benefit__label">Capital<br>Spend</span>
  </div>
  <div class="benefit col-left" style="top:350px">
    <span class="benefit__icon"><svg viewBox="0 0 48 48"><path d="M24 4a20 20 0 1 0 0 40 20 20 0 0 0 0-40zm0 5a15 15 0 0 1 14.6 12H30a6 6 0 0 0-12 0H9.4A15 15 0 0 1 24 9zM9.6 27h6.6l4 10.5A15 15 0 0 1 9.6 27zm18.2 10.5 4-10.5h6.6a15 15 0 0 1-10.6 10.5z"/></svg></span>
    <span class="benefit__label">Driver<br>Safty</span>
  </div>
  <div class="benefit col-right" style="top:350px">
    <span class="benefit__icon"><svg viewBox="0 0 48 48"><circle cx="24" cy="14" r="8"/><path d="M8 44c0-10 6-17 16-17s16 7 16 17z"/><path d="M22 27h4l1 12-3 3-3-3z" fill="#fff"/></svg></span>
    <span class="benefit__label">Customer<br>Satisfaction</span>
  </div>
  <div class="benefit col-left" style="top:458px">
    <span class="benefit__icon"><svg viewBox="0 0 48 48"><rect x="6" y="34" width="7" height="8"/><rect x="16" y="29" width="7" height="13"/><rect x="26" y="23" width="7" height="19"/><rect x="36" y="16" width="7" height="26"/><path d="M6 26 18 18l6 3 14-13" stroke="#4a4a4a" stroke-width="2.5" fill="none"/><path d="M33 6h8v8z"/></svg></span>
    <span class="benefit__label">Bottom<br>Line Profit</span>
  </div>
  <div class="benefit col-right" style="top:458px">
    <span class="benefit__icon"><svg viewBox="0 0 48 48"><rect x="10" y="4" width="28" height="40"/><g fill="#e0b06a"><rect x="14" y="8" width="5" height="5"/><rect x="21.5" y="8" width="5" height="5"/><rect x="29" y="8" width="5" height="5"/><rect x="14" y="16" width="5" height="5"/><rect x="21.5" y="16" width="5" height="5"/><rect x="29" y="16" width="5" height="5"/><rect x="14" y="24" width="5" height="5"/><rect x="21.5" y="24" width="5" height="5"/><rect x="29" y="24" width="5" height="5"/><rect x="14" y="32" width="5" height="5"/><rect x="29" y="32" width="5" height="5"/><rect x="21.5" y="34" width="5" height="10"/></g></svg></span>
    <span class="benefit__label">Organisation<br>Expectations</span>
  </div>

  <div class="benefit benefit--reduce col-left" style="top:618px">
    <span class="benefit__icon"><svg viewBox="0 0 48 48"><path d="M23 44V22h2v22z"/><path d="M24 22c-1-7 2-14 6-16 1 7-1 13-6 16z"/><path d="M23 30c-6 0-10-4-11-10 6 0 10 4 11 10z"/><path d="M25 34c1-6 5-10 11-10-1 6-5 10-11 10z"/></svg></span>
    <span class="benefit__label">Carbon<br>Footprints</span>
  </div>
  <div class="benefit benefit--reduce col-right" style="top:618px">
    <span class="benefit__icon"><svg viewBox="0 0 48 48"><rect x="6" y="8" width="30" height="30" rx="2"/><rect x="10" y="12" width="22" height="22" fill="#bbb"/><circle cx="21" cy="23" r="5"/><rect x="9" y="38" width="5" height="4"/><rect x="28" y="38" width="5" height="4"/><g fill="#e3a52a"><rect x="37" y="26" width="8" height="4"/><rect x="37" y="31" width="8" height="4"/><rect x="37" y="36" width="8" height="4"/></g></svg></span>
    <span class="benefit__label">Business<br>Overheads</span>
  </div>
  <div class="benefit benefit--reduce col-left" style="top:730px">
    <span class="benefit__icon"><svg viewBox="0 0 48 48"><path d="M28 4 14 27h9l-3 17 14-24h-9z"/></svg></span>
    <span class="benefit__label">Company<br>Risk</span>
  </div>
  <div class="benefit benefit--reduce col-right" style="top:730px">
    <span class="benefit__icon"><svg viewBox="0 0 48 48"><text x="24" y="38" font-size="36" font-family="Arial" font-weight="700" text-anchor="middle">$</text></svg></span>
    <span class="benefit__label">Operational<br>Costs</span>
  </div>
  <div class="benefit benefit--reduce col-left" style="top:843px">
    <span class="benefit__icon"><svg viewBox="0 0 48 48"><path d="M4 12a3 3 0 0 1 3-3h34a3 3 0 0 1 3 3v24a3 3 0 0 1-3 3H7a3 3 0 0 1-3-3zm4 3v4h32v-4zm0 15v3h12v-3zm22 0v3h4v-3zm6 0v3h4v-3z" fill-rule="evenodd"/></svg></span>
    <span class="benefit__label">Speeding<br>Tickets</span>
  </div>

  <h2 class="heading heading--decrease">Decrease<br>Your</h2>
</main>
</body>
</html>
```